Electrician Company Website Design

I am looking to get a website designed only. I do not need it converted ot html. I simply need the design in a psd format. I have my own team for the conversion. The website is for an electrician company called Bramblecourt electric. I have created a txt document with the project parameters and specifics. I have also uploaded their logo in all avaible formats. It's a zip file.

Number of Pages Required

1 page

```html
<!DOCTYPE html>
<html lang="en">
<head>
<meta charset="utf-8">
<title>Bramblecourt Electric</title>
<link rel="stylesheet" href="https://fonts.googleapis.com/css2?family=Lato:wght@400;700;900&family=Poppins:wght@600;700&display=swap">
<style>
:root{
  --blue:#1566b9;
  --blue-deep:#0f57a6;
  --navy:#0c3566;
  --bright:#1b7fdc;
  --gold:#f2b21e;
  --ink:#1e2a36;
  --white:#ffffff;
  --photo-a:#8c9aa8;
  --photo-b:#5c6c86;
}
*{margin:0;padding:0;box-sizing:border-box}
html,body{width:1200px;height:2964px;overflow:hidden}
body{position:relative;font-family:'Lato',sans-serif;color:var(--ink);background:var(--white)}
.abs{position:absolute}
a{color:inherit;text-decoration:none}

/* top bar */
.topbar{left:0;top:0;width:1200px;height:49px;background:var(--blue);color:var(--white);font-size:15px}
.topbar .social{left:110px;top:13px;display:flex;gap:9px}
.dot{width:21px;height:21px;border-radius:50%;background:var(--white)}
.topbar .item{top:14px;display:flex;align-items:center;gap:8px}
.topbar svg{fill:var(--white)}

/* header */
.header{left:0;top:49px;width:1200px;height:94px;background:var(--white)}
.brand-tab{left:112px;top:49px;width:143px;height:114px;background:var(--white);border-radius:0 0 14px 14px;box-shadow:0 3px 6px rgba(0,0,0,.08);display:flex;flex-direction:column;align-items:center;justify-content:center;gap:8px;z-index:3}
.brand-mark{width:46px;height:46px;border-radius:50%;background:var(--navy)}
.brand-name{font-weight:900;font-size:14px;color:var(--navy);text-align:center;line-height:1.2}
.nav{top:86px;left:497px;display:flex;gap:23px;font-size:17px;color:var(--ink)}
.btn{display:flex;align-items:center;justify-content:center;background:var(--blue);color:var(--white);font-weight:700;border-radius:2px}
.nav-cta{left:955px;top:77px;width:129px;height:38px;font-size:16px}

/* hero */
.hero-photo{left:0;top:143px;width:1200px;height:665px;background:linear-gradient(100deg,#7a6a5a 0%,#a69d92 30%,#4d6fb9 45%,#c9c4bb 70%,#8d8a86 100%)}
.hero-cut{left:0;top:700px;width:1200px;height:110px}
.touch{left:744px;top:190px;width:414px;height:473px;background:rgba(255,255,255,.35);border-radius:10px}
.touch-panel{left:750px;top:197px;width:402px;height:463px;background:var(--blue);border-radius:8px;color:var(--white)}
.touch-panel h2{position:absolute;top:38px;width:100%;text-align:center;font-family:'Poppins',sans-serif;font-weight:600;font-size:24px;letter-spacing:.5px}
.touch-panel .bar{position:absolute;left:157px;top:84px;width:88px;height:3px;background:var(--gold)}
.field{position:absolute;left:37px;width:328px;height:48px;background:var(--white);border-radius:8px;color:#333;font-size:15px;padding:15px 22px}
.submit{position:absolute;left:137px;top:377px;width:129px;height:38px;background:var(--navy);color:var(--white);font-weight:900;font-size:16px;display:flex;align-items:center;justify-content:center;border-radius:2px}

/* company */
.ring{left:100px;top:816px;width:400px;height:400px;border-radius:50%;background:var(--blue)}
.ring-photo{left:128px;top:838px;width:372px;height:372px;border-radius:50%;background:linear-gradient(135deg,#c9d2dc,#6f8aa6 55%,#2f5e9c);border:4px solid var(--white)}
.ring-dot{left:396px;top:1148px;width:86px;height:86px;border-radius:50%;background:var(--blue)}
.h-section{font-family:'Poppins',sans-serif;font-weight:700;letter-spacing:1px}
.company-title{left:590px;top:866px;font-size:40px;color:var(--bright)}
.company-text{left:590px;top:930px;width:489px;font-size:16.5px;line-height:30px;text-align:justify}
.company-btn{left:590px;top:1167px;width:169px;height:58px;font-size:17px}

/* service area */
.area{left:0;top:1303px;width:1200px;height:474px;background:linear-gradient(135deg,var(--blue) 0%,#1a6cc3 50%,var(--blue-deep) 100%)}
.area-title{left:160px;top:1340px;font-size:38px;color:var(--white)}
.area-text{left:161px;top:1408px;width:440px;font-size:21px;line-height:34.5px;color:var(--white)}
.area-list{top:1578px;display:flex;flex-direction:column;gap:17px;color:var(--white);font-size:18px}
.area-list li{list-style:none;display:flex;align-items:center;gap:12px;height:23px}
.area-list svg{fill:var(--white);flex:none}
.area-hl{left:409px;top:1569px;width:168px;height:42px;background:rgba(255,255,255,.12);border:1px solid rgba(255,255,255,.25)}
.map{left:655px;top:1340px;width:425px;height:415px;background:linear-gradient(160deg,#f4f6f9,#dfe4ea);border-radius:6px;box-shadow:6px 10px 0 #0c47a0}

/* quote */
.quote-title{left:145px;top:1832px;font-size:39px;color:var(--bright)}
.quote-text{left:252px;top:1915px;width:819px;font-size:15.2px;line-height:28.5px;text-align:justify}
.quote-btn{left:907px;top:2033px;width:169px;height:58px;font-size:17px}

/* services */
.services{left:0;top:2150px;width:1200px;height:550px;background:linear-gradient(135deg,#1566b9,#1a6cc3 60%,#1160b4);overflow:hidden;color:var(--white)}
.services-title{position:absolute;left:0;top:45px;width:100%;text-align:center;font-size:39px}
.card{position:absolute;top:118px;width:420px}
.card .count{font-size:19px;font-weight:700}
.card .count span{color:var(--navy);font-weight:700}
.card h3{margin-top:21px;font-family:'Lato',sans-serif;font-weight:700;font-size:34px;white-space:nowrap}
.card p{margin-top:23px;width:300px;font-size:16.2px;line-height:28.4px}
.card .more{position:absolute;top:330px;left:2px;display:flex;align-items:center;gap:14px;font-weight:900;font-size:17px}
.card svg{stroke:var(--white);fill:none}
.svc-frame{position:absolute;left:600px;top:235px;width:224px;height:200px;border-top:6px solid var(--white);border-right:6px solid var(--white)}
.svc-photo{position:absolute;left:452px;top:240px;width:364px;height:244px;background:linear-gradient(120deg,#3b4650,#7d8a94 40%,#c0392b 55%,#1f56b8 75%,#283a8a);border:2px solid var(--white)}

/* footer */
.f-brand{left:82px;top:2738px;display:flex;align-items:center;gap:10px}
.f-brand .brand-mark{width:40px;height:40px}
.f-brand span{font-weight:900;font-size:17px;color:var(--navy)}
.f-follow{left:107px;top:2834px;font-size:17px;font-weight:700;color:var(--navy)}
.f-social{left:106px;top:2870px;display:flex;gap:5px}
.f-social .dot{width:34px;height:34px;background:none;border:2px solid var(--blue)}
.f-copy{left:106px;top:2929px;font-size:12.5px}
.f-col h4{font-weight:400;font-size:17px;margin-bottom:12px;color:var(--navy)}
.f-col li{list-style:none;display:flex;align-items:center;gap:14px;height:31px;font-size:17px}
.f-col li svg{stroke:var(--blue);fill:none;flex:none}
.f-contact .row{display:flex;gap:24px;font-size:17px;line-height:30px;margin-bottom:8px}
.f-contact svg{fill:var(--blue);flex:none;margin-top:7px}
</style>
</head>
<body>

<!-- top bar -->
<div class="abs topbar">
  <div class="abs social"><span class="dot"></span><span class="dot"></span><span class="dot"></span></div>
  <div class="abs item" style="left:690px"><svg width="20" height="20" viewBox="0 0 20 20"><circle cx="10" cy="10" r="10"/></svg>Pricing</div>
  <div class="abs item" style="left:794px"><svg width="24" height="22" viewBox="0 0 24 22"><path d="M3 12a9 9 0 0 1 18 0v6h-4v-7h2a7 7 0 0 0-14 0h2v7H3z"/></svg></div>
  <div class="abs item" style="left:842px;font-size:14px">Call Us: +1 555 014 2290</div>
  <div class="abs item" style="left:1019px"><svg width="22" height="22" viewBox="0 0 22 22"><circle cx="11" cy="11" r="11"/></svg>Login</div>
</div>

<!-- header -->
<div class="abs header"></div>
<div class="abs brand-tab"><span class="brand-mark"></span><span class="brand-name">Bramblecourt<br>Electric</span></div>
<nav class="abs nav"><a>Company</a><a>Service Area</a><a>Services</a><a>Gallery</a><a>FAQs</a></nav>
<a class="abs btn nav-cta">CONTACT US</a>

<!-- hero -->
<div class="abs hero-photo" role="img" aria-label="Two smiling electricians in blue work uniforms and caps holding cables and a toolbox in front of a house"></div>
<svg class="abs hero-cut" viewBox="0 0 1200 110" width="1200" height="110" preserveAspectRatio="none">
  <polygon points="0,110 0,98 270,8 1200,100 1200,110" fill="#ffffff"/>
  <polygon points="0,98 270,8 1200,100 1200,106 270,30 0,110" fill="#1566b9"/>
  <polygon points="0,96 270,6 1200,96 1200,100 270,8 0,98" fill="#1566b9" opacity=".5"/>
</svg>
<div class="abs touch"></div>
<form class="abs touch-panel">
  <h2>Get In Touch</h2>
  <span class="bar"></span>
  <div class="field" style="top:124px">Name</div>
  <div class="field" style="top:184px">Phone</div>
  <div class="field" style="top:244px">Email ID</div>
  <div class="field" style="top:304px">Address</div>
  <div class="submit">SUBMIT</div>
</form>

<!-- company -->
<div class="abs ring"></div>
<div class="abs ring-photo" role="img" aria-label="Young electrician in a blue cap working at an electrical control panel"></div>
<div class="abs ring-dot"></div>
<h2 class="abs h-section company-title">COMPANY</h2>
<p class="abs company-text">Neque porro quisquam est, qui dolorem ipsum quia dolor sit amet, consectetur, adipisci velit, sed quia non numquam eius modi tempora incidunt ut labore et dolore magnam aliquam quaerat voluptatem. Neque porro quisquam est, qui dolorem ipsum quia dolor sit amet, consectetur, adipisci velit, sed quia non numquam eius modi tempora incidunt ut labore et dolore magnam aliquam quaerat voluptatem.</p>
<a class="abs btn company-btn">LEARN MORE</a>

<!-- service area -->
<div class="abs area"></div>
<h2 class="abs h-section area-title">SERVICE AREA</h2>
<p class="abs area-text">Providing quality, professional general contracting and home remodeling services in the following Minnesota and the surrounding counties</p>
<div class="abs area-hl"></div>
<ul class="abs area-list" style="left:164px">
  <li><svg width="14" height="19" viewBox="0 0 14 19"><path d="M7 0a7 7 0 0 1 7 7c0 5-7 12-7 12S0 12 0 7a7 7 0 0 1 7-7zm0 4a3 3 0 1 0 0 6 3 3 0 0 0 0-6z"/></svg>Almelund MN</li>
  <li><svg width="14" height="19" viewBox="0 0 14 19"><path d="M7 0a7 7 0 0 1 7 7c0 5-7 12-7 12S0 12 0 7a7 7 0 0 1 7-7zm0 4a3 3 0 1 0 0 6 3 3 0 0 0 0-6z"/></svg>Blaine MN</li>
  <li><svg width="14" height="19" viewBox="0 0 14 19"><path d="M7 0a7 7 0 0 1 7 7c0 5-7 12-7 12S0 12 0 7a7 7 0 0 1 7-7zm0 4a3 3 0 1 0 0 6 3 3 0 0 0 0-6z"/></svg>Cambridge MN</li>
  <li><svg width="14" height="19" viewBox="0 0 14 19"><path d="M7 0a7 7 0 0 1 7 7c0 5-7 12-7 12S0 12 0 7a7 7 0 0 1 7-7zm0 4a3 3 0 1 0 0 6 3 3 0 0 0 0-6z"/></svg>Chisago City MN</li>
</ul>
<ul class="abs area-list" style="left:420px;top:1577px">
  <li><svg width="14" height="19" viewBox="0 0 14 19"><path d="M7 0a7 7 0 0 1 7 7c0 5-7 12-7 12S0 12 0 7a7 7 0 0 1 7-7zm0 4a3 3 0 1 0 0 6 3 3 0 0 0 0-6z"/></svg>Forest Lake MN</li>
  <li><svg width="14" height="19" viewBox="0 0 14 19"><path d="M7 0a7 7 0 0 1 7 7c0 5-7 12-7 12S0 12 0 7a7 7 0 0 1 7-7zm0 4a3 3 0 1 0 0 6 3 3 0 0 0 0-6z"/></svg>Fridley MN</li>
  <li><svg width="14" height="19" viewBox="0 0 14 19"><path d="M7 0a7 7 0 0 1 7 7c0 5-7 12-7 12S0 12 0 7a7 7 0 0 1 7-7zm0 4a3 3 0 1 0 0 6 3 3 0 0 0 0-6z"/></svg>Harris MN</li>
  <li><svg width="14" height="19" viewBox="0 0 14 19"><path d="M7 0a7 7 0 0 1 7 7c0 5-7 12-7 12S0 12 0 7a7 7 0 0 1 7-7zm0 4a3 3 0 1 0 0 6 3 3 0 0 0 0-6z"/></svg>Hugo MN</li>
</ul>
<div class="abs map" role="img" aria-label="3D map of Minnesota and surrounding states with blue location pins marking service areas"></div>

<!-- quote -->
<h2 class="abs h-section quote-title">GET A QUOTE</h2>
<p class="abs quote-text">Sed ut perspiciatis unde omnis iste natus error sit voluptatem accusantium doloremque laudantium, totam rem aperiam, eaque ipsa quae ab illo inventore veritatis et quasi architecto beatae vitae dicta sunt explicabo. Nemo enim ipsam voluptatem quia voluptas sit aspernatur aut odit aut fugit, sed quia consequuntur magni dolores eos qui ratione voluptatem sequi nesciunt.</p>
<a class="abs btn quote-btn">QUOTE NOW</a>

<!-- services -->
<section class="abs services">
  <h2 class="h-section services-title">OUR SERVICES</h2>
  <article class="card" style="left:108px">
    <div class="count">01 <span>/ 03</span></div>
    <h3>Commerical Electrical Services</h3>
    <p>Sed ut perspiciatis unde omnis iste natu error sit voluptatem accus doloremque laudantium, totam rem aperiam, eaque ipsa quae ab illo inventore veritat quasi architecto beatae vitae dictt explicabo. Nemo enim ipsam voluptatem voluptas.</p>
    <a class="more">LEARN MORE <svg width="30" height="14" viewBox="0 0 30 14" stroke-width="2"><circle cx="5" cy="7" r="4"/><path d="M9 7h19M22 2l6 5-6 5"/></svg></a>
  </article>
  <div class="svc-frame"></div>
  <div class="svc-photo" role="img" aria-label="Technician in gloves servicing commercial equipment with gauges and a red meter"></div>
  <article class="card" style="left:1008px">
    <div class="count">02 <span>/ 03</span></div>
    <h3>Residential Electrical Services</h3>
    <p>Sed ut perspiciatis unde omnis iste natu error sit voluptatem accus doloremque laudantium, totam rem aperiam, eaque ipsa quae ab illo inventore veritat quasi architecto beatae vitae dictt explicabo. Nemo enim ipsam voluptatem voluptas.</p>
    <a class="more">LEARN MORE <svg width="30" height="14" viewBox="0 0 30 14" stroke-width="2"><circle cx="5" cy="7" r="4"/><path d="M9 7h19M22 2l6 5-6 5"/></svg></a>
  </article>
</section>

<!-- footer -->
<div class="abs f-brand"><span class="brand-mark"></span><span>Bramblecourt Electric</span></div>
<div class="abs f-follow">FOLLOW US</div>
<div class="abs f-social"><span class="dot"></span><span class="dot"></span><span class="dot"></span></div>
<div class="abs f-copy">2022 Bramblecourt Electric. All Rights Reserved.</div>

<div class="abs f-col" style="left:428px;top:2744px">
  <h4>QUICK LINKS</h4>
  <ul>
    <li><svg width="14" height="12" viewBox="0 0 14 12" stroke-width="1.6"><path d="M1 1l5 5-5 5M7 1l5 5-5 5"/></svg>Company</li>
    <li><svg width="14" height="12" viewBox="0 0 14 12" stroke-width="1.6"><path d="M1 1l5 5-5 5M7 1l5 5-5 5"/></svg>Service Area</li>
    <li><svg width="14" height="12" viewBox="0 0 14 12" stroke-width="1.6"><path d="M1 1l5 5-5 5M7 1l5 5-5 5"/></svg>Services</li>
    <li><svg width="14" height="12" viewBox="0 0 14 12" stroke-width="1.6"><path d="M1 1l5 5-5 5M7 1l5 5-5 5"/></svg>Gallery</li>
    <li><svg width="14" height="12" viewBox="0 0 14 12" stroke-width="1.6"><path d="M1 1l5 5-5 5M7 1l5 5-5 5"/></svg>FAQs</li>
  </ul>
</div>
<div class="abs f-col" style="left:624px;top:2744px">
  <h4>OTHER LINKS</h4>
  <ul>
    <li><svg width="14" height="12" viewBox="0 0 14 12" stroke-width="1.6"><path d="M1 1l5 5-5 5M7 1l5 5-5 5"/></svg>Tearms &amp; Condition</li>
    <li><svg width="14" height="12" viewBox="0 0 14 12" stroke-width="1.6"><path d="M1 1l5 5-5 5M7 1l5 5-5 5"/></svg>Privacy Policy</li>
    <li><svg width="14" height="12" viewBox="0 0 14 12" stroke-width="1.6"><path d="M1 1l5 5-5 5M7 1l5 5-5 5"/></svg>Cookies</li>
    <li><svg width="14" height="12" viewBox="0 0 14 12" stroke-width="1.6"><path d="M1 1l5 5-5 5M7 1l5 5-5 5"/></svg>FAQs</li>
  </ul>
</div>
<div class="abs f-col f-contact" style="left:872px;top:2744px">
  <h4>CONTACT</h4>
  <div class="row"><svg width="16" height="21" viewBox="0 0 14 19"><path d="M7 0a7 7 0 0 1 7 7c0 5-7 12-7 12S0 12 0 7a7 7 0 0 1 7-7zm0 4a3 3 0 1 0 0 6 3 3 0 0 0 0-6z"/></svg><span>1420 Alder Row NE<br>Norvale, MN 55099</span></div>
  <div class="row"><svg width="16" height="16" viewBox="0 0 16 16"><path d="M3 0l3 4-2 2c1 2 4 5 6 6l2-2 4 3-2 3C7 16 0 9 0 3z"/></svg><span>+1 555 014 2290</span></div>
  <div class="row"><svg width="16" height="12" viewBox="0 0 16 12"><path d="M0 0h16v12H0zM0 1l8 6 8-6"/></svg><span>info@bramblecourt.com</span></div>
</div>

</body>
</html>
```